I already have a logo created by Quillory Makers that I'm very happy with. I need to spruce up my business card now. Its a double sided card with not much info on it, I like to keep it simple.
Front of card: name, phone # email address, web address. Tag Line "Outsourced Technology Solutions", under that it says Business Voice Services & Electronic Protection.
Rear of Card: Content written inside a "cloud" saying "Cloud Solutions" "Cloud Integrity"

Target Market(s)

Business to Business

Industry/Entity Type

Business

Contact Information for Business Card

We are in the technology field. Providing Telephone systems (hardware), SIP Trunks (dial tone/local/long distance/telephone #'s), LAN (Local Area Network)infrastructure cabling, Data Center solutions and Security Applications (Camera systems, Access Control systems,

Requirements
Must have
• Must have brevity
Should not have
• Clutter and/or too much information

```html
<!DOCTYPE html>
<html lang="en">
<head>
<meta charset="utf-8">
<title>Veridane Signal Works – Business Card</title>
<link href="https://fonts.googleapis.com/css2?family=Raleway:wght@400;700&family=Roboto:wght@400;500&display=swap" rel="stylesheet">
<style>
  :root {
    --navy: #1f3f7f;
    --blue-light: #6b93d2;
    --grey-band: #a9a9ab;
    --grey-text: #8a8a8e;
    --backdrop: #dcdde0;
    --white: #ffffff;
    --faint: #c9cbe0;
  }
  * { margin: 0; padding: 0; box-sizing: border-box; }
  html, body { width: 1200px; height: 800px; overflow: hidden; }
  body {
    background: var(--backdrop);
    font-family: "Roboto", Arial, sans-serif;
    position: relative;
  }
  .card {
    position: absolute;
    top: 250px;
    width: 525px;
    height: 300px;
    border-radius: 4px;
    overflow: hidden;
    box-shadow: 0 6px 18px rgba(0,0,0,.12);
  }
  /* Front */
  .card-front { left: 45px; background: var(--white); }
  .brand {
    position: absolute; left: 0; right: 0; top: 28px;
    text-align: center;
  }
  .brand-name {
    display: inline-flex; align-items: center; gap: 10px;
    font-family: "Raleway", Arial, sans-serif;
    font-weight: 700; font-size: 25px; color: var(--navy);
  }
  .brand-mark { width: 16px; height: 16px; background: var(--navy); }
  .tagline {
    font-family: "Raleway", Arial, sans-serif;
    color: var(--grey-text); font-size: 16px; margin-top: 6px;
  }
  .subline {
    font-family: "Raleway", Arial, sans-serif;
    color: var(--grey-text); font-size: 11px; margin-top: 3px;
  }
  .rule-top {
    position: absolute; left: 0; right: 0; top: 118px; height: 4px;
    background: var(--navy);
  }
  .band {
    position: absolute; left: 0; right: 0; top: 128px; height: 122px;
    background: var(--navy);
    border-top: 3px solid var(--navy);
  }
  .band::before {
    content: ""; position: absolute; left: 0; right: 0; top: 6px; height: 2px;
    background: var(--white);
  }
  .person {
    position: absolute; left: 40px; top: 42px; width: 190px; text-align: right;
    color: var(--white);
  }
  .person-name { font-size: 22px; font-weight: 500; }
  .person-role { font-size: 14px; margin-top: 2px; }
  .divider {
    position: absolute; left: 250px; top: 34px; width: 1px; height: 66px;
    background: rgba(255,255,255,.45);
  }
  .contacts {
    position: absolute; left: 268px; top: 34px; list-style: none;
    color: var(--white); font-size: 14px;
  }
  .contacts li { display: flex; align-items: center; gap: 8px; height: 22px; }
  .contacts svg { width: 13px; height: 13px; }
  .address-band {
    position: absolute; left: 0; right: 0; bottom: 0; height: 46px;
    background: var(--grey-band); border-top: 4px solid var(--white);
    color: var(--white); font-size: 14px;
    display: flex; align-items: center; padding-left: 120px;
  }
  /* Back */
  .card-back {
    left: 630px;
    background: linear-gradient(160deg, var(--blue-light) 0%, #3d66b0 55%, var(--navy) 100%);
  }
  .cloud { position: absolute; left: 40px; top: 30px; width: 445px; height: 250px; }
  .cloud-text {
    position: absolute; left: 0; right: 0; top: 125px; text-align: center;
    font-family: "Raleway", Arial, sans-serif;
  }
  .cloud-text .brand-name { color: var(--faint); font-size: 20px; }
  .cloud-text .brand-mark { background: var(--faint); width: 13px; height: 13px; }
  .cloud-text .tagline { color: var(--faint); font-size: 13px; }
  .cloud-text .subline { color: var(--faint); font-size: 9px; }
</style>
</head>
<body>

<section class="card card-front" aria-label="Business card front">
  <div class="brand">
    <div class="brand-name"><span class="brand-mark"></span>Veridane Signal Works, LLC</div>
    <div class="tagline">Outsourced Technology Solutions</div>
    <div class="subline">Business Voice Services &amp; Electronic Protection</div>
  </div>
  <div class="rule-top"></div>
  <div class="band">
    <div class="person">
      <div class="person-name">Marlo Fenwick</div>
      <div class="person-role">Director Operations</div>
    </div>
    <div class="divider"></div>
    <ul class="contacts">
      <li>
        <svg viewBox="0 0 13 13" aria-hidden="true"><rect width="13" height="13" rx="2" fill="#a9a9ab"/><path d="M4 3l1.5 0 .6 2-1 .7a5 5 0 0 0 2.3 2.3l.7-1 2 .6V9.5C10 10 9.5 10.3 9 10.2 6 9.8 3.3 7 2.9 4 2.8 3.5 3.2 3 4 3z" fill="#fff"/></svg>
        555 014 7720
      </li>
      <li>
        <svg viewBox="0 0 13 13" aria-hidden="true"><rect width="13" height="13" rx="2" fill="#a9a9ab"/><rect x="2.5" y="4" width="8" height="5.5" fill="none" stroke="#fff"/><path d="M2.5 4l4 3 4-3" fill="none" stroke="#fff"/></svg>
        hollowpine.net
      </li>
      <li>
        <svg viewBox="0 0 13 13" aria-hidden="true"><rect width="13" height="13" rx="2" fill="#a9a9ab"/><circle cx="6.5" cy="6.5" r="3.8" fill="none" stroke="#fff"/><path d="M2.7 6.5h7.6M6.5 2.7c-2 2.4-2 5.2 0 7.6M6.5 2.7c2 2.4 2 5.2 0 7.6" fill="none" stroke="#fff" stroke-width=".8"/></svg>
        www.hollowpine.net
      </li>
    </ul>
  </div>
  <div class="address-band">48 Larkspur Lane, Eastbrook 10477</div>
</section>

<section class="card card-back" aria-label="Business card back">
  <svg class="cloud" viewBox="0 0 445 250" aria-hidden="true">
    <path fill="#fff" d="M60 250 C10 250 0 200 10 170 C20 135 55 120 80 125 C70 75 110 30 165 40 C190 5 260 0 290 40 C330 25 380 50 380 100 C430 110 450 170 430 210 C418 238 395 250 370 250 Z"/>
  </svg>
  <div class="cloud-text">
    <div class="brand-name"><span class="brand-mark"></span>Veridane Signal Works, LLC</div>
    <div class="tagline">Outsourced Technology Solutions</div>
    <div class="subline">Business Voice Services &amp; Electronic Protection</div>
  </div>
</section>

</body>
</html>
```